Yellow Page Ad

We require a two full page,full colour, side by side yellow page ad.
Each page is sized 259mm[H]x210mm[W]
This would be listed under the "wholesale distributor" section of the yellow pages.

We are a wholesale distribution company.
Please see attached a past sketch of this ad we have created, however our director did not like.

The following are the departments we would like to highlight:
1.General Variety Mechandise
2.Corporate Promotional Items
3.Beverages
4.Complete Packaging Solutions(Restuarant & Fast Food Packaging)

For your reference, we have also attached our company profile.

```html
<!DOCTYPE html>
<html lang="en">
<head>
<meta charset="utf-8">
<title>Northvale Trading Ltd – Directory Ad, Page 2</title>
<link href="https://fonts.googleapis.com/css2?family=Arimo:wght@400;700&display=swap" rel="stylesheet">
<style>
  :root {
    --stage: #ece8e2;
    --page: #dfe5f1;
    --navy: #2b4a8e;
    --navy-dark: #23407f;
    --white: #ffffff;
    --ink: #1c2f63;
    --photo-warehouse: linear-gradient(135deg, #c9b98a 0%, #8d9aa8 50%, #e5dfcf 100%);
    --photo-bottles: radial-gradient(circle at 50% 55%, #6b7f3a 0%, #9a6b3c 35%, #eef0ea 75%);
    --photo-showroom: linear-gradient(180deg, #d9dde3 0%, #b9bfc7 45%, #eef0f2 100%);
  }
  * { box-sizing: border-box; margin: 0; padding: 0; }
  html, body { width: 1200px; height: 1000px; overflow: hidden; }
  body {
    background: var(--stage);
    font-family: "Arimo", Arial, sans-serif;
    font-weight: 700;
    color: var(--navy);
    position: relative;
  }
  .ad-page {
    position: absolute;
    left: 230px; top: 24px;
    width: 740px; height: 953px;
    background: var(--page);
    overflow: hidden;
  }
  .brand { position: absolute; left: 28px; top: 8px; width: 320px; height: 150px; }
  .brand__disc {
    position: absolute; left: 4px; top: 4px;
    width: 118px; height: 118px; border-radius: 50%;
    background: var(--navy);
  }
  .brand__name {
    position: absolute; left: 132px; top: 44px;
    font-size: 30px; color: var(--navy); line-height: 1.05;
  }
  .brand__tagline {
    position: absolute; left: 48px; top: 132px;
    font-size: 16px; color: var(--ink);
  }
  .contact {
    position: absolute; right: 4px; top: 22px; width: 420px;
    text-align: center; font-size: 20px; line-height: 27px; color: var(--navy);
  }
  .section-title { position: absolute; font-size: 33px; color: var(--navy); }
  .section-sub { position: absolute; font-size: 20px; color: var(--navy); }
  .info-box {
    position: absolute; background: var(--navy);
    color: var(--white); font-size: 16px; line-height: 22px;
    text-align: center; border-radius: 14px;
    display: flex; align-items: center; justify-content: center;
  }
  .photo-disc {
    position: absolute; width: 154px; height: 154px; border-radius: 50%;
    border: 4px solid var(--white); box-shadow: 0 0 0 2px #1d1d1d;
  }
  .photo-disc--warehouse { background: var(--photo-warehouse); }
  .photo-disc--bottles { background: var(--photo-bottles); }
  .showroom-band {
    position: absolute; left: 0; top: 690px; width: 740px; height: 132px;
    background: var(--photo-showroom);
  }
  .cta {
    position: absolute; left: 0; top: 826px; width: 740px;
    text-align: center; font-size: 34px; color: var(--navy-dark);
  }
  .hours {
    position: absolute; left: 0; top: 860px; width: 740px;
    text-align: center; font-size: 21px; color: var(--navy-dark);
  }
  .partner-strip {
    position: absolute; left: 0; top: 885px; width: 740px; height: 68px;
    background: var(--white);
  }
</style>
</head>
<body>
  <main class="ad-page">
    <header class="brand">
      <div class="brand__disc"></div>
      <div class="brand__name">Northvale<br>Trading Ltd</div>
      <div class="brand__tagline">Your global sourcing experts!</div>
    </header>

    <address class="contact" style="font-style:normal">
      Telephone No.: (868) 555-0142<br>
      Fax No.: (868) 555-0177<br>
      E-Mail: sales@northvaletrading.example<br>
      Website: www.northvaletrading.example
    </address>

    <h1 class="section-title" style="left:13px; top:186px;">Complete Packaging Solutions</h1>
    <p class="section-sub" style="left:13px; top:228px;">(Restaurant &amp; Fast Food Packaging)</p>

    <div class="info-box" style="left:170px; top:274px; width:554px; height:144px; padding:0 20px 0 60px;">
      With Over 6,000 active accounts inclusive of top chains , supermarkets, variety stores, specialty stores, discount marts, convenience stores, phar-macies, hotels, restaurants, bars, other retailers, wholesalers, businesses in the food service, we provide complete packaging for all.
    </div>
    <div class="photo-disc photo-disc--warehouse" style="left:16px; top:293px;" role="img" aria-label="Photo of a warehouse interior with stacked stock and yellow racking"></div>

    <h2 class="section-title" style="left:535px; top:464px;">Beverages</h2>

    <div class="info-box" style="left:22px; top:522px; width:570px; height:144px; padding:0 70px 0 10px;">
      Within our beverage department, we also represent Multinational companies and global brands like Harbor Light, keldmark,silverspring, red lantern, tiderock, marlo and many more high quality brands to ensure our customers are satisfied
    </div>
    <div class="photo-disc photo-disc--bottles" style="left:545px; top:505px;" role="img" aria-label="Photo of assorted beer, wine and spirit bottles"></div>

    <div class="showroom-band" role="img" aria-label="Panoramic photo of a bright retail showroom with white display shelving"></div>

    <p class="cta">Visit our new 100,000 ft showroom TODAY!</p>
    <p class="hours">Mon-Fri: 8:30am-43:30pm Sat: 8:30-2:30 Sun-Seasonal</p>

    <footer class="partner-strip">
      <svg width="740" height="68" viewBox="0 0 740 68" aria-label="Partner brands">
        <g fill="#c9ced8">
          <circle cx="18" cy="45" r="13"/>
          <circle cx="46" cy="42" r="15"/>
          <rect x="64" y="38" width="42" height="14" rx="3"/>
          <rect x="112" y="38" width="36" height="14" rx="3"/>
          <rect x="152" y="38" width="34" height="14" rx="3"/>
          <rect x="190" y="38" width="28" height="14" rx="3"/>
          <rect x="222" y="38" width="32" height="14" rx="3"/>
          <rect x="258" y="38" width="38" height="14" rx="3"/>
          <rect x="300" y="34" width="26" height="20" rx="3"/>
          <rect x="330" y="34" width="28" height="20" rx="3"/>
          <rect x="370" y="36" width="36" height="16" rx="2"/>
          <rect x="410" y="36" width="32" height="16" rx="2"/>
          <rect x="446" y="36" width="28" height="16" rx="2"/>
          <rect x="478" y="36" width="34" height="16" rx="2"/>
          <rect x="516" y="30" width="30" height="28" rx="3"/>
          <rect x="550" y="32" width="24" height="24" rx="3"/>
          <rect x="578" y="36" width="32" height="16" rx="3"/>
          <circle cx="624" cy="44" r="12"/>
          <circle cx="650" cy="42" r="12"/>
          <rect x="666" y="34" width="28" height="20" rx="3"/>
          <rect x="698" y="30" width="34" height="28" rx="3"/>
        </g>
      </svg>
    </footer>
  </main>
</body>
</html>
```